KLO Threads Holiday Card

Holiday card for our Textile company. Our corporate colors are orange and blue. See www.klothreads.example for what we do. Basically we take flat man-made yarn and texture it to look and feel like wool or cotton. Our yarn is wound on an 11 inch cardboard tube (see website for pictures).

Industry/Entity Type

It Company

```html
<!DOCTYPE html>
<html lang="en">
<head>
<meta charset="utf-8">
<title>KLO Threads Holiday Card</title>
<link href="https://fonts.googleapis.com/css2?family=Bebas+Neue&family=Open+Sans:ital,wght@0,400;0,600;0,700;1,400&display=swap" rel="stylesheet">
<style>
  :root {
    --page-bg: #ebe8e4;
    --card-white: #ffffff;
    --sky-top: #ffffff;
    --sky-mid: #a9d6e2;
    --sky-bottom: #3f9bb5;
    --snow: #f7f7f5;
    --brand-blue: #1763ad;
    --brand-orange: #f0682a;
    --ink: #3b3b3b;
    --ink-soft: #555555;
    --rule: #cfcfcf;
    --photo-dark: #4a4f55;
    --photo-light: #c9ccd0;
  }
  * { margin: 0; padding: 0; box-sizing: border-box; }
  html, body { width: 1200px; height: 986px; overflow: hidden; }
  body {
    position: relative;
    background: var(--page-bg);
    font-family: "Open Sans", Arial, sans-serif;
  }
  .card {
    position: absolute;
    width: 543px;
    height: 410px;
    overflow: hidden;
    box-shadow: 0 2px 6px rgba(0,0,0,0.18);
  }

  /* Front */
  .card-front {
    left: 99px; top: 69px;
    background: linear-gradient(180deg, var(--sky-top) 0%, var(--sky-mid) 45%, var(--sky-bottom) 100%);
  }
  .snowflake-art {
    position: absolute; left: 0; top: 0; width: 385px; height: 150px;
    background: radial-gradient(ellipse at 30% 30%, rgba(255,255,255,0.85) 0%, rgba(255,255,255,0) 70%);
  }
  .front-brand {
    position: absolute; right: 33px; top: 46px;
    display: flex; align-items: center; gap: 7px;
    font-weight: 700; font-size: 22px; color: var(--brand-blue);
  }
  .brand-dot { width: 14px; height: 14px; border-radius: 50%; background: var(--brand-orange); }
  .greeting-rule {
    position: absolute; height: 1.5px; background: rgba(255,255,255,0.95);
  }
  .rule-top { left: 97px; top: 191px; width: 348px; }
  .rule-bottom-left { left: 97px; top: 320px; width: 148px; }
  .rule-bottom-right { left: 297px; top: 320px; width: 148px; }
  .greeting-main {
    position: absolute; left: 97px; top: 196px; width: 348px;
    text-align: center; white-space: nowrap;
    font-family: "Bebas Neue", Impact, sans-serif;
    font-weight: 400;
    font-size: 88px; line-height: 88px; color: #fff;
    letter-spacing: 0.5px;
  }
  .greeting-sub {
    position: absolute; left: 67px; top: 273px; width: 408px;
    text-align: center; white-space: nowrap;
    font-family: "Bebas Neue", Impact, sans-serif;
    font-size: 40px; line-height: 40px; color: #fff;
  }
  .greeting-sub-text {
    display: inline-block;
    transform: scaleX(0.82);
    transform-origin: center;
  }
  .deer-art {
    position: absolute; left: 483px; top: 330px; width: 40px; height: 54px;
    background: rgba(255,255,255,0.85); border-radius: 4px;
  }
  .snow-hills { position: absolute; left: 0; bottom: 0; width: 543px; height: 60px; }

  /* Back */
  .card-back { left: 543px; top: 519px; background: var(--card-white); }
  .back-brand {
    position: absolute; left: 31px; top: 58px;
    display: flex; align-items: center; gap: 7px;
    font-weight: 700; font-size: 20px; color: var(--brand-blue);
  }
  .machine-photo {
    position: absolute; left: 30px; top: 122px; width: 186px; height: 74px;
    border-radius: 8px;
    background: linear-gradient(180deg, var(--photo-light) 0%, #8e9399 45%, var(--photo-dark) 100%);
  }
  .headline {
    position: absolute; left: 30px; top: 206px; width: 190px;
    font-weight: 700; font-size: 18.5px; line-height: 22px; color: var(--brand-blue);
    white-space: nowrap;
  }
  .subhead {
    position: absolute; left: 30px; top: 228px; width: 190px;
    font-weight: 700; font-size: 13.4px; line-height: 18px; color: var(--brand-orange);
    white-space: nowrap;
  }
  .about {
    position: absolute; left: 30px; top: 250px; width: 186px;
    font-style: italic; font-size: 9.6px; line-height: 12.6px; color: var(--ink-soft);
    text-align: justify;
  }
  .contact-call {
    position: absolute; left: 30px; top: 304px; width: 190px;
    font-weight: 600; font-size: 11px; line-height: 13.6px; color: var(--brand-blue);
  }
  .contact-list {
    position: absolute; left: 30px; top: 340px; list-style: none;
    font-size: 11px; line-height: 15.5px; color: var(--ink);
  }
  .contact-list .note { color: var(--brand-orange); }
  .contact-list .address { font-size: 9.5px; line-height: 16px; color: var(--ink-soft); }
  .divider {
    position: absolute; left: 243px; top: 38px; width: 1px; height: 342px; background: var(--rule);
  }
  .stamp-box {
    position: absolute; left: 453px; top: 39px; width: 56px; height: 56px;
    border: 1px solid #e3e3e3;
  }
  .to-label {
    position: absolute; left: 324px; top: 117px; font-size: 10px; color: var(--ink);
  }
  .address-line {
    position: absolute; left: 334px; width: 174px; height: 1px; background: #dcdcdc;
  }
</style>
</head>
<body>

<section class="card card-front" aria-label="Holiday card front">
  <div class="snowflake-art" role="img" aria-label="Soft white snowflakes drifting across the winter sky"></div>
  <div class="front-brand"><span class="brand-dot"></span>KLO Threads</div>
  <div class="greeting-rule rule-top"></div>
  <h1 class="greeting-main">Wishing You</h1>
  <p class="greeting-sub"><span class="greeting-sub-text">A Wonderful Holiday Season</span></p>
  <div class="greeting-rule rule-bottom-left"></div>
  <div class="greeting-rule rule-bottom-right"></div>
  <div class="deer-art" role="img" aria-label="White silhouette of a standing deer on the snow"></div>
  <svg class="snow-hills" viewBox="0 0 543 60" preserveAspectRatio="none" aria-hidden="true">
    <path d="M0 10 C90 -2 220 8 380 48 L380 60 L0 60 Z" fill="var(--snow)"/>
    <path d="M240 60 C300 38 420 28 543 32 L543 60 Z" fill="var(--snow)"/>
    <path d="M0 60 L0 38 C140 30 300 40 378 58 L380 60 Z" fill="#ffffff"/>
  </svg>
</section>

<section class="card card-back" aria-label="Holiday card back">
  <div class="back-brand"><span class="brand-dot"></span>KLO Threads</div>
  <div class="machine-photo" role="img" aria-label="Photo of yarn texturing machines winding yarn onto cardboard tubes"></div>
  <h2 class="headline">IDEAS &amp; INNOVATION</h2>
  <p class="subhead">ENGINEERED TO PERFECTION</p>
  <p class="about">KLO Threads develops and processes air jet textured, commingled &amp; interlaced continuous fiber and spun yarns to precise custom specifications.</p>
  <p class="contact-call">Contact us for textured yarns<br>that enhance your performance</p>
  <ul class="contact-list">
    <li>800-555-0142 <span class="note">(toll free)</span></li>
    <li>540-555-0187 <span class="note">(local)</span></li>
    <li class="address">P.O. Box 1200, Riverton, VA 24000</li>
  </ul>
  <div class="divider"></div>
  <div class="stamp-box"></div>
  <span class="to-label">To</span>
  <div class="address-line" style="top:162px"></div>
  <div class="address-line" style="top:190px"></div>
  <div class="address-line" style="top:215px"></div>
  <div class="address-line" style="top:243px"></div>
</section>

</body>
</html>
```